Meadowlark Dental Letterhead

Please design full color letterhead for meadowlark dental. Letterhead should match the motif of the business card. Print and logo should be confined to a one inch margin on top and bottom. The following info should be included:
Medowlark Dental with the tooth logo
Curtis L. Ferrell, DDS
Gentle Hands Always, Friendly Faces Daily
Phone #: 555.276.4158
Address: 20354-C N Larkspur, Fernvale, KS

```html
<!DOCTYPE html>
<html lang="en">
<head>
<meta charset="utf-8">
<title>Meadowlark Dental Letterhead</title>
<link rel="stylesheet" href="https://fonts.googleapis.com/css2?family=Open+Sans:wght@400;600;700&display=swap">
<style>
  :root {
    --backdrop: #e4e4e6;
    --paper: #ffffff;
    --ink: #3a3a3a;
    --ink-soft: #8a8a8a;
    --brand-blue: #3572b9;
    --brand-red: #e2513a;
    --brand-green: #62bb5e;
    --signature-tone: #d9d9d9;
  }
  * { box-sizing: border-box; margin: 0; padding: 0; }
  html, body {
    width: 1200px; height: 1000px; overflow: hidden;
    background: var(--backdrop);
    font-family: "Open Sans", Arial, sans-serif;
    color: var(--ink);
  }
  .letterhead {
    position: absolute; left: 229px; top: 20px;
    width: 742px; height: 960px;
    background: var(--paper);
    box-shadow: 0 6px 24px rgba(0,0,0,0.12);
    overflow: hidden;
  }
  .brand {
    position: absolute; top: 58px; right: 150px;
    text-align: left;
  }
  .brand-name {
    display: flex; align-items: center; gap: 8px;
    font-size: 19px; font-weight: 700; color: var(--brand-blue);
    letter-spacing: 0.5px;
  }
  .brand-mark {
    width: 16px; height: 16px; border-radius: 50%;
    background: var(--brand-green);
  }
  .brand-lines {
    margin-left: 24px; margin-top: 3px;
    font-size: 9.5px; line-height: 13px; color: var(--ink-soft);
  }
  .letter {
    position: absolute; top: 190px; left: 80px; right: 80px;
    font-size: 10.5px; line-height: 15px;
  }
  .letter-title {
    text-align: center; font-weight: 700; font-size: 11px;
    margin-bottom: 14px; padding-left: 110px;
  }
  .letter-grid { display: flex; gap: 18px; }
  .sidebar { width: 92px; text-align: right; color: var(--ink-soft); }
  .sidebar strong { color: var(--ink); display: block; }
  .letter-body { flex: 1; }
  .letter-body p { margin-bottom: 14px; text-align: justify; }
  .signoff { margin-top: 30px; padding-left: 100px; font-size: 8px; color: var(--ink-soft); }
  .signature {
    width: 90px; height: 24px; border-radius: 4px;
    background: var(--signature-tone); margin-bottom: 3px;
  }
  .contact {
    position: absolute; bottom: 128px; right: 70px;
    display: flex; gap: 34px; font-size: 10.5px;
  }
  .footer-band {
    position: absolute; left: 0; bottom: 0;
    width: 742px; height: 100px;
    background: linear-gradient(90deg, var(--brand-red) 0%, var(--brand-blue) 40%, var(--brand-green) 100%);
  }
</style>
</head>
<body>
  <main class="letterhead">
    <header class="brand">
      <div class="brand-name"><span class="brand-mark"></span>Meadowlark Dental</div>
      <div class="brand-lines">
        Curtis L. Ferrell, DDS<br>
        Gentle Hands Always<br>
        Friendly Faces Daily
      </div>
    </header>

    <section class="letter">
      <h1 class="letter-title">Lorem ipsum dolor sit amet, el eros vidit sonet eum</h1>
      <div class="letter-grid">
        <aside class="sidebar">
          <strong>Lorem ipsum</strong>
          Dolor sit amet eros vidit sonet sed
        </aside>
        <div class="letter-body">
          <p>Lorem ipsum dolor sit amet, el eros vidit sonet eum, sed ea aliquam offendit. Neque quando lobortis sed in, no solum ceteros est. Accumsan pertinacia an qui, te vidisse recteque pro, cu per habemus officiis, eos ex malis posidonium similique. Appetere principes eloquentiam vis ei, an mea alia petentium dignissim, te justo omnium duo.</p>
          <p>Movet laoreet delicatissimi cum id. Essent dissentiet cu cum, atqui augue iriure qui ea. Liber propriae et sed. Euismod ornatus scaevola et pro.</p>
          <p>Verterem interesset disputationi vim et, laudem persecuti quo eu. Mea viderer vulputate ut. Ad scripta scaevola appetere usu, omnium forensibus sed cu, dolorum admodum postulant mea ei. Eos ut ubique graeco insolens, etiam electram assentior cum at.</p>
          <p>In eos solum verterem facilisis, magna scaevola explicari has ex, at vidisse percipitur cum. At dicam postea luptatum sea, sed te timeam principes disputando, postea scaevola eloquentiam quo eu. Cetero concludaturque cu ius, nam erat detraxit ut, in his cetero vocent erroribus. Eu sint nulla comprehensam qui. Dolor dolorum splendide ei est, id usu inani liber deterruisset.</p>
          <p>Omnis intellegat intellegam duo cu, no ornatus partiendo referrentur has.</p>
        </div>
      </div>
      <div class="signoff">
        <div class="signature" role="img" aria-label="Handwritten signature"></div>
        Curtis L. Ferrell, DDS
      </div>
    </section>

    <footer class="contact">
      <span>Phone #: 555.276.4158</span>
      <span>Address: 20354-C N Larkspur, Fernvale, KS</span>
    </footer>

    <div class="footer-band" role="img" aria-label="Decorative footer band in red, blue and green"></div>
  </main>
</body>
</html>
```